VORLANE (PTY)LTD Website design

WEBSITE design based on our different divisions in our organization.
Our company specializes in the following.
Construction
Property development
Demolition
Mining
Transport
Manufacturing of concrete bricks and blocks
Lightweight concrete Readymix
I want a very modern website and look that fits in with our organization and the changing times of the world.
The website must be very professional and crisp and should appeal to both the younger generation and older generation of business leaders and.
The website must be very user friendly and easy to navigate, simple yet modern, professional and corporate.

```html
<!DOCTYPE html>
<html lang="en">
<head>
<meta charset="utf-8">
<title>VORLANE (PTY)LTD</title>
<link href="https://fonts.googleapis.com/css2?family=Montserrat:ital,wght@0,400;0,500;0,600;0,700;0,800;1,400&display=swap" rel="stylesheet">
<style>
:root{
  --blue:#29a8e0;
  --blue-deep:#1f8fd0;
  --ink:#3f4246;
  --muted:#8a8d91;
  --rule:#d9dbdd;
  --white:#ffffff;
  --footer:#343536;
  --footer-text:#d6d6d6;
}
*{margin:0;padding:0;box-sizing:border-box}
html,body{width:1200px;height:2861px;overflow:hidden;background:var(--white)}
body{position:relative;font-family:'Montserrat',sans-serif;color:var(--ink)}
.abs{position:absolute}

/* header */
.site-header{position:absolute;left:0;top:0;width:1200px;height:118px;border-bottom:4px solid var(--blue-deep)}
.brand{left:172px;top:34px;font-size:44px;font-weight:800;color:var(--blue-deep);letter-spacing:1px;display:flex;align-items:center;gap:10px}
.brand-square{width:14px;height:14px;background:var(--blue-deep)}
.call{right:177px;top:26px;font-size:20px;font-weight:700;color:#8a8d91;display:flex;align-items:center;gap:6px}
.call strong{color:var(--blue);font-weight:700}
.nav{top:80px;left:0;width:1200px}
.nav a{position:absolute;font-size:12px;font-weight:500;color:#2d2f33;text-decoration:none}
.nav a.active{color:var(--blue)}

/* hero */
.hero{left:0;top:118px;width:1200px;height:485px;background:linear-gradient(100deg,#b9b0a4 0%,#a59a8e 30%,#b59f55 55%,#6b6b55 75%,#c0b3a0 100%)}
.hero-title{left:174px;top:288px;font-size:54px;font-weight:800;color:var(--white)}
.hero-sub{left:170px;top:352px;font-size:30px;font-weight:500;color:var(--white)}
.dots{left:567px;top:566px;display:flex;gap:6px}
.dots span{width:12px;height:12px;border-radius:50%;background:var(--white)}
.dots span.on{background:var(--blue)}

/* section heads */
.section-title{left:0;width:1200px;text-align:center;font-size:24px;font-weight:700;color:var(--ink)}
.section-title em{font-style:normal;color:var(--blue-deep)}
.section-lede{left:0;width:1200px;text-align:center;font-size:13.5px;line-height:22px;color:var(--muted)}

/* services */
.tile{position:absolute;width:276px}
.tile-photo{width:100%}
.tile-label{width:100%;height:62px;background:var(--blue);color:var(--white);font-size:15.5px;font-weight:600;display:flex;align-items:center;justify-content:center;text-align:center;line-height:20px}

/* testimonial */
.rule{left:172px;width:855px;height:1px;background:var(--rule)}
.quote{left:0;width:1200px;text-align:center;top:1792px;font-size:14.5px;line-height:23.5px;font-style:italic;color:var(--muted)}
.author{left:0;width:1200px;text-align:center;top:1900px;font-size:14px;font-weight:600;color:var(--blue)}

/* news */
.news{position:absolute;width:267px}
.news-photo{width:100%;height:163px}
.news-head{margin-top:19px;margin-left:1px;border-left:3px solid var(--blue-deep);border-top:3px solid var(--blue-deep);border-bottom:3px solid var(--blue-deep);border-right:0;padding:8px 0 5px 16px;position:relative}
.news-head::after{content:"";position:absolute;left:0;top:-3px;width:33px;height:3px;background:var(--blue-deep)}
.news-date{font-size:13px;font-weight:600;color:var(--blue-deep);line-height:15px}
.news-title{font-size:13.5px;font-weight:700;color:#222;line-height:16px}
.news-body{margin-top:16px;padding-left:2px;font-size:11px;line-height:21.5px;color:#555}

/* footer */
.site-footer{left:0;top:2522px;width:1200px;height:339px;background:radial-gradient(ellipse at 55% 40%,#4a4a4a 0%,var(--footer) 70%)}
.f-brand{left:172px;top:2574px;font-size:44px;font-weight:800;color:var(--white);display:flex;align-items:center;gap:10px}
.f-brand .brand-square{background:var(--white)}
.social{left:173px;top:2667px;display:flex;gap:8px}
.social span{width:29px;height:29px;border-radius:50%;background:#232425}
.f-head{top:2566px;font-size:14px;font-weight:500;color:var(--white)}
.f-text{font-size:11px;line-height:19.5px;color:var(--footer-text)}
.f-links{font-size:11px;line-height:24px;color:var(--footer-text)}
.email-label{left:698px;top:2688px;font-size:10.5px;font-style:italic;color:var(--footer-text)}
.email-line{left:698px;top:2711px;width:164px;height:1px;background:#6a6a6a}
.signup{left:698px;top:2730px;width:100px;height:37px;border-radius:19px;background:var(--blue);color:var(--white);font-size:12.5px;font-weight:600;display:flex;align-items:center;justify-content:center}
.f-rule{left:162px;top:2800px;width:876px;height:1px;background:#555}
.copyright{left:0;width:1200px;top:2825px;text-align:center;font-size:11px;color:var(--footer-text)}
</style>
</head>
<body>

<header class="site-header">
  <div class="abs brand"><span>VORLANE</span><span class="brand-square"></span></div>
  <div class="abs call">
    <svg width="18" height="18" viewBox="0 0 24 24" aria-hidden="true"><path fill="#29a8e0" d="M6.6 10.8a15.1 15.1 0 0 0 6.6 6.6l2.2-2.2a1 1 0 0 1 1-.25 11.4 11.4 0 0 0 3.6.57 1 1 0 0 1 1 1V20a1 1 0 0 1-1 1A17 17 0 0 1 3 4a1 1 0 0 1 1-1h3.5a1 1 0 0 1 1 1c0 1.25.2 2.45.57 3.6a1 1 0 0 1-.25 1z"/></svg>
    <span>Call Us:<strong>0400555128</strong></span>
  </div>
  <nav class="abs nav">
    <a class="active" style="left:503px">HOME</a>
    <a style="left:581px">SERVICES</a>
    <a style="left:681px">BLOG</a>
    <a style="left:754px">ABOUT US</a>
    <a style="left:858px">CLIENTS</a>
    <a style="left:948px">CONTACT US</a>
  </nav>
</header>

<section>
  <div class="abs hero" role="img" aria-label="Smiling site engineer in hard hat and hi-vis vest on a construction site with machinery behind"></div>
  <div class="abs hero-title">VORLANE</div>
  <div class="abs hero-sub">MOVING MOUNTAINS</div>
  <div class="abs dots"><span></span><span></span><span></span><span class="on"></span></div>
</section>

<section>
  <h2 class="abs section-title" style="top:660px">OUR <em>SERVICES</em></h2>
  <p class="abs section-lede" style="top:700px">Lorem ipsum dolor sit amet, consectetur adipiscing elit, sed do eiusmod<br>tempor incididunt ut labore et dolore magna aliquad minim</p>

  <div class="tile" style="left:172px;top:839px">
    <div class="tile-photo" style="height:352px;background:linear-gradient(180deg,#8fa3b6 0%,#c9a477 55%,#e08a2c 75%,#2a1d14 100%)" role="img" aria-label="Silhouetted workers on a steel frame at sunset"></div>
    <div class="tile-label">Construction</div>
  </div>
  <div class="tile" style="left:172px;top:1268px">
    <div class="tile-photo" style="height:240px;background:linear-gradient(160deg,#5e6f80 0%,#7a7f82 50%,#9b8a66 100%)" role="img" aria-label="Excavator demolishing a concrete building"></div>
    <div class="tile-label">Demolition</div>
  </div>

  <div class="tile" style="left:462px;top:801px">
    <div class="tile-photo" style="height:208px;background:linear-gradient(170deg,#a99c8c 0%,#8c7f6f 50%,#b0a040 80%,#6f6454 100%)" role="img" aria-label="Mining shovel loading a haul truck in an open pit"></div>
    <div class="tile-label">Mining</div>
  </div>
  <div class="tile" style="left:462px;top:1084px">
    <div class="tile-photo" style="height:173px;background:linear-gradient(180deg,#6aa6dc 0%,#d8e2e8 50%,#7fae52 100%)" role="img" aria-label="Modern house rising from architectural plans"></div>
    <div class="tile-label">Property development</div>
  </div>
  <div class="tile" style="left:462px;top:1333px">
    <div class="tile-photo" style="height:218px;background:linear-gradient(180deg,#2e4566 0%,#c99a4e 45%,#556b3e 65%,#3a3c40 100%)" role="img" aria-label="Truck driving on a highway at sunset"></div>
    <div class="tile-label">Transport</div>
  </div>

  <div class="tile" style="left:751px;top:839px">
    <div class="tile-photo" style="height:240px;background:linear-gradient(160deg,#8d4a36 0%,#b65d40 50%,#9a9088 100%)" role="img" aria-label="Gloved hand laying bricks on mortar"></div>
    <div class="tile-label">Manufacturing of concrete<br>bricks and blocks</div>
  </div>
  <div class="tile" style="left:751px;top:1154px">
    <div class="tile-photo" style="height:353px;background:linear-gradient(180deg,#c9b347 0%,#8f8b86 35%,#a09c96 70%,#7f7b76 100%)" role="img" aria-label="Wet concrete pouring down a chute"></div>
    <div class="tile-label">Lightweight<br>concrete Readymix</div>
  </div>
</section>

<section>
  <div class="abs rule" style="top:1690px"></div>
  <svg class="abs" style="left:575px;top:1733px" width="50" height="36" viewBox="0 0 50 36" aria-hidden="true">
    <path fill="#1f8fd0" d="M11 36a11 11 0 0 1-11-11C0 12 8 3 18 0l2 4c-6 3-9 7-9 10a11 11 0 0 1 0 22zm27 0a11 11 0 0 1-11-11C27 12 35 3 45 0l2 4c-6 3-9 7-9 10a11 11 0 0 1 0 22z"/>
  </svg>
  <svg class="abs" style="left:305px;top:1812px" width="20" height="38" viewBox="0 0 20 38" aria-hidden="true"><path d="M18 1 2 19l16 18" fill="none" stroke="#c4c6c8" stroke-width="1.5"/></svg>
  <svg class="abs" style="left:882px;top:1812px" width="20" height="38" viewBox="0 0 20 38" aria-hidden="true"><path d="M2 1l16 18L2 37" fill="none" stroke="#c4c6c8" stroke-width="1.5"/></svg>
  <p class="abs quote">At vero eos et accusamus et iusto odio dignissimos ducimus qui blanditiis<br>praesentium voluptatum deleniti atque corrupti quos dolores et quas mole<br>stias excepturi sint occaecati cupiditate non provident, similique sunt in<br>culpa qui officia deserunt mollitia animi, id est laboru.</p>
  <p class="abs author">Dana Wells , City Name</p>
  <div class="abs rule" style="top:1977px"></div>
</section>

<section>
  <h2 class="abs section-title" style="top:2036px">LATEST <em>NEWS</em></h2>
  <p class="abs section-lede" style="top:2078px">Lorem ipsum dolor sit amet, consectetadipcing elit, sed do eiusmod<br>tempor incididunutlabore et dolore magna aliquad minim</p>

  <article class="news" style="left:172px;top:2151px">
    <div class="news-photo" style="background:linear-gradient(150deg,#6a5a48 0%,#b9b2a6 50%,#c8b04a 100%)" role="img" aria-label="Worker laying paving blocks"></div>
    <div class="news-head"><div class="news-date">DEC 17 2018</div><div class="news-title">SED UT PERSPICIATISUTUS ATEM.</div></div>
    <p class="news-body">Sed ut perspiciatis unde omnis issit voluptat<br>em accusantium dorspiciatis unde omnis issit<br>voluptaem accusantium dolorntilornt</p>
  </article>
  <article class="news" style="left:467px;top:2151px">
    <div class="news-photo" style="background:linear-gradient(180deg,#5f7a9c 0%,#b88a5e 55%,#7b5a44 100%)" role="img" aria-label="Timber-framed house under construction"></div>
    <div class="news-head"><div class="news-date">DEC 17 2018</div><div class="news-title">SED UT PERSPICIATISUTUS ATEM.</div></div>
    <p class="news-body">Sed ut perspiciatis unde omnis issit voluptat<br>em accusantium dorspiciatis unde omnis issit<br>voluptaem accusantium dolorntilornt</p>
  </article>
  <article class="news" style="left:759px;top:2151px">
    <div class="news-photo" style="background:linear-gradient(180deg,#7d9bc4 0%,#b9c3cc 40%,#c79a2c 65%,#55504a 100%)" role="img" aria-label="Yellow haul truck at a quarry"></div>
    <div class="news-head"><div class="news-date">DEC 17 2018</div><div class="news-title">SED UT PERSPICIATISUTUS ATEM.</div></div>
    <p class="news-body">Sed ut perspiciatis unde omnis issit voluptat<br>em accusantium dorspiciatis unde omnis issit<br>voluptaem accusantium dolorntilornt</p>
  </article>
</section>

<footer>
  <div class="abs site-footer" role="img" aria-label="Dimmed photo of a worker on a dusty site"></div>
  <div class="abs f-brand"><span>VORLANE</span><span class="brand-square"></span></div>
  <div class="abs social" aria-label="Social links"><span></span><span></span><span></span><span></span></div>

  <h3 class="abs f-head" style="left:431px">ABOUT US</h3>
  <p class="abs f-text" style="left:431px;top:2605px">Morbi pharetra blandit faucibure<br>eros turpis, scelerisque in nisl anatis<br>blandit sem. Cras quis dui vitae puus<br>interdum sollicitudin ut ut odiolerisqu<br>ein nisl anatis blandit semas quis dui<br>vitae puus interdum sollictut od.</p>

  <h3 class="abs f-head" style="left:698px">NEWSLETTER</h3>
  <p class="abs f-text" style="left:698px;top:2605px">Subscribe to us to get and<br>receive the latest news, sales<br>and updates.</p>
  <div class="abs email-label">Email Address:</div>
  <div class="abs email-line"></div>
  <div class="abs signup">SIGN UP</div>

  <h3 class="abs f-head" style="left:928px">LINKS</h3>
  <p class="abs f-links" style="left:928px;top:2603px">Sed ut perspiciatis<br>Unde omnis iste natus<br>Voluptatem accusan<br>Tium doloremque<br>Haudantium<br>Tum doloremque</p>

  <div class="abs f-rule"></div>
  <p class="abs copyright">© 2018 All rights are reserved. Privacy | Terms of use</p>
</footer>

</body>
</html>
```